K-12 Education site

We are looking for a Wordpress theme that does the following:
- Uses our school colors: green and gold/yellow (not a true requirement as these colors can be pretty ugly)
- Works on all mobile devices and scales properly
- We are an Arts and Technology school so we would like the design to be clean, vibrant, and yet make use of HTML5
- Unique design

Target Market(s)

Prospective students and current students

Industry/Entity Type

School

Requirements
Must have
• Clean and unique Design
HTML5
Must scale for mobile devices

```html
<!DOCTYPE html>
<html lang="en">
<head>
<meta charset="utf-8">
<title>Riverbend Regional Academy</title>
<link href="https://fonts.googleapis.com/css2?family=Arimo:wght@400;700&display=swap" rel="stylesheet">
<style>
:root{
  --green-dark:#0b4611;
  --green:#0d4a14;
  --green-text:#4f8f3a;
  --green-link:#3f9a2a;
  --gold:#d9b21c;
  --ink:#222;
  --muted:#8a8a8a;
  --rule:#d7e5e6;
  --white:#fff;
}
*{box-sizing:border-box;margin:0;padding:0}
html,body{width:842px;height:1200px;overflow:hidden;background:var(--white)}
body{position:relative;font-family:"Arimo",Arial,sans-serif;color:var(--ink)}
.abs{position:absolute}
ul{list-style:none}
a{color:inherit;text-decoration:none}

/* header */
.brand-mark{left:74px;top:22px;width:96px;display:flex;align-items:center;gap:5px}
.brand-mark span{width:12px;height:12px;border-radius:50%;background:var(--gold);flex:none}
.brand-mark b{font-size:11px;font-weight:700;color:var(--green);line-height:1.2}
.site-title{left:184px;top:34px;font-size:22.5px;font-weight:700;line-height:22px;color:var(--green);letter-spacing:.2px}
.site-sub{left:187px;top:82px;font-size:6.5px;font-weight:700;color:var(--ink)}
.search{left:630px;top:25px;width:134px;height:25px;border:1px solid #cfcfcf;font-size:8px;color:#999;padding:8px 9px}
.search svg{position:absolute;right:8px;top:5px}
.top-links{right:76px;top:84px;display:flex;gap:10px;font-size:7px;font-weight:700;color:#333}

/* nav */
.main-nav{left:67px;top:109px;width:702px;height:35px;background:var(--green);display:flex;align-items:center;padding-left:23px;gap:0}
.main-nav a{color:var(--white);font-size:8.5px;font-weight:700;margin-right:23.5px}

.hero{left:67px;top:144px;width:702px;height:298px;background:linear-gradient(180deg,#cfc6b8 0%,#8b6a47 45%,#2f4a30 62%,#a47445 100%)}
.hero-dots{right:83px;top:414px;display:flex;gap:2px}
.hero-dots i{width:8px;height:6px;background:#eee;display:block}

.divider{left:67px;width:702px;height:4px;border-top:1px solid var(--rule);border-bottom:2px solid var(--rule)}

.section-title{font-size:12.5px;font-weight:700;color:var(--green);letter-spacing:.2px}

/* welcome */
.welcome-photo{left:82px;top:487px;width:409px;height:85px;background:linear-gradient(90deg,#6a4a36,#b58c6c 30%,#55524a 55%,#c7966a 80%,#5b3b2a)}
.welcome-lead{left:82px;top:581px;width:420px;font-size:10.8px;line-height:14px;color:var(--green-text)}
.welcome-text{left:83px;top:616px;width:410px;font-size:8.3px;line-height:11px;color:#333}
.welcome-text a{color:var(--green-link)}

/* news */
.news-intro{left:523px;top:494px;width:250px;font-size:7.8px;line-height:12.3px;color:#222;word-break:break-all}
.news-list{left:523px;top:557px;width:246px}
.news-list li{font-size:7.8px;font-weight:700;color:var(--green-link);padding:4px 0 4px 16px;border-bottom:1px solid #eee;position:relative;height:19px}
.news-list li:last-child{border-bottom:none}
.arrow{position:absolute;left:5px;top:7px}

/* services */
.service-photo{width:94px;height:94px}
.service-title{font-size:10.8px;color:var(--green-text)}
.service-text{width:296px;font-size:7.9px;line-height:11.2px;color:var(--muted)}
.service-text a{display:block;color:#222}
.service-rule{left:82px;top:819px;width:393px;height:1px;background:#ccc}

/* programs */
.program-photo{left:524px;top:710px;width:235px;height:95px;background:linear-gradient(180deg,#6f9a4a 0%,#9bb872 40%,#a9a0a0 70%,#7e8a80 100%)}
.program-text{left:523px;top:813px;width:245px;font-size:7.9px;line-height:11.3px;color:var(--muted)}
.program-list{top:872px;font-size:8.4px;font-weight:700;color:#222}
.program-list li{position:relative;padding-left:14px;height:17px}
.program-list .arrow{left:0;top:3px}

/* footer */
.footer{left:0;top:1022px;width:842px;height:151px;background:var(--green-dark)}
.footer-head{font-size:8.8px;font-weight:700;color:var(--white)}
.footer-links{font-size:8.4px;font-weight:700;color:#c7d2c6;line-height:16.9px}
.footer-links.alt{color:#b4c1b3}
.subscribe{left:597px;top:1037px;font-size:7.5px;font-weight:700;color:var(--white)}
.field{left:599px;width:135px;height:25px;background:var(--white);border:1px solid #ccc}
.socials{left:624px;top:1135px;display:flex;gap:3px}
.socials span{width:26px;height:26px;border-radius:50%;background:#e6e6e6;border:2px solid #bdbdbd;display:block}
.copyright{left:94px;top:1181px;font-size:8.3px;color:#888}
</style>
</head>
<body>

<header>
  <div class="abs brand-mark"><span></span><b>Riverbend</b></div>
  <h1 class="abs site-title">RIVERBEND REGIONAL<br>ACADEMY</h1>
  <p class="abs site-sub">FOR THE ARTS &amp; TECHNOLOGY &nbsp;| &nbsp;140 N. ELM ST, 20100 555.010.0200</p>
  <div class="abs search">Search
    <svg width="12" height="12" viewBox="0 0 12 12"><circle cx="5" cy="5" r="3.6" fill="none" stroke="#aaa" stroke-width="1.5"/><line x1="7.6" y1="7.6" x2="11" y2="11" stroke="#aaa" stroke-width="1.8"/></svg>
  </div>
  <nav class="abs top-links"><a>RRA EMAIL</a><a>CALENDARS</a><a>CONTACT US</a><a>SUBSCRIBE/NEWSLETTERS</a></nav>
</header>

<nav class="abs main-nav">
  <a>HOME</a><a>ABOUT RRA</a><a>STUDENTS / PARENTS</a><a>FACULTY / STAFF</a><a>DOCUMENTS / FORMS</a><a>PROGRAMS OF STUDY</a><a>SERVICES</a>
</nav>

<div class="abs hero" role="img" aria-label="Dance team students posing with trophies in the school gym"></div>
<div class="abs hero-dots"><i></i><i></i><i></i><i></i><i></i></div>

<div class="abs divider" style="top:453px"></div>

<h2 class="abs section-title" style="left:81px;top:469px">WELCOME TO OUR SCHOOL</h2>
<div class="abs welcome-photo" role="img" aria-label="Students working at desks in a classroom"></div>
<p class="abs welcome-lead">LOREM IPSUM DOLOR SIT AMET, CONSECTETUR ADIPISICING ELIT, SED DO INCIDIDUNT UT LABORE ET DOLORE MAGNA ALIQUA. UT ENIM</p>
<p class="abs welcome-text">Lorem ipsum dolor sit amet, consectetur adipisicing elit, sed do eiusmod tempor incididunt ut labore et dolore magna aliqua. Ut enim ad minim veniam, quis nostrud. <a>Learn More</a></p>

<h2 class="abs section-title" style="left:524px;top:469px">LATEST NEWS</h2>
<p class="abs news-intro">Please keep your letter handy and follow this link: https://forms.riverbend-example.org/sign/enroll?formId=a71c42de-5d08-4e1b-9c33-7f20b6e1d90a<br>Do not use this link unless you were instructed to do so on your recent mailing or by the main office.</p>
<ul class="abs news-list">
  <li><svg class="arrow" width="7" height="5" viewBox="0 0 7 5"><path d="M0 2.5H6M4 .5 6 2.5 4 4.5" stroke="#333" fill="none" stroke-width=".8"/></svg>Girls' volleyball tryouts will begin on Monday, August 5th</li>
  <li><svg class="arrow" width="7" height="5" viewBox="0 0 7 5"><path d="M0 2.5H6M4 .5 6 2.5 4 4.5" stroke="#333" fill="none" stroke-width=".8"/></svg>Student Materials Fees List for 2013-2014</li>
  <li><svg class="arrow" width="7" height="5" viewBox="0 0 7 5"><path d="M0 2.5H6M4 .5 6 2.5 4 4.5" stroke="#333" fill="none" stroke-width=".8"/></svg>Art Trading Card Exhibition features over 100 original</li>
</ul>

<div class="abs divider" style="top:663px"></div>

<h2 class="abs section-title" style="left:84px;top:687px">SERVICES</h2>
<div class="abs service-photo" style="left:82px;top:710px;background:linear-gradient(135deg,#5d6b3a,#c9a58a 45%,#d8397a 75%,#4e5a30)" role="img" aria-label="Student holding books outdoors"></div>
<h3 class="abs service-title" style="left:187px;top:709px;font-weight:400">INFORMATION TECHNOLOGY</h3>
<p class="abs service-text" style="left:188px;top:729px">Lorem ipsum dolor sit amet, consectetur adipisicing elit, sed do eiusmod tempor incididunt ut labore et dolore magna aliqua. Ut enim ad minim veniam, quis nostrud. Lorem ipsum dolor sit amet. Lorem ipsum dolor sit amet, consectetur adipisicing elit, sed do eiusmod tempor incididunt ut l abore et dolore magna aliqua.<a>Read more..</a></p>
<div class="abs service-rule"></div>
<div class="abs service-photo" style="left:83px;top:836px;background:linear-gradient(135deg,#3d3d3d,#7a6a5e 45%,#c8202e 80%,#2f2f2f)" role="img" aria-label="Student at a chalkboard with math equations"></div>
<h3 class="abs service-title" style="left:187px;top:836px;font-weight:400">LIBRARY &amp; MANAGEMENT</h3>
<p class="abs service-text" style="left:188px;top:856px">Lorem ipsum dolor sit amet, consectetur adipisicing elit, sed do eiusmod tempor incididunt ut labore et dolore magna aliqua. Ut enim ad minim veniam, quis nostrud. Lorem ipsum dolor sit amet. Lorem ipsum dolor sit amet, consectetur adipisicing elit, sed do eiusmod tempor incididunt ut l abore et dolore magna aliqua.<a>Read more..</a></p>

<h2 class="abs section-title" style="left:524px;top:687px">PROGRAMS OF STUDY</h2>
<div class="abs program-photo" role="img" aria-label="Group of students reading together on a bench in a park"></div>
<p class="abs program-text">The Visual Arts Program encourages innovation while stressing strong technical and presentation skills. The prog-ram also promotes an awareness of current issues and ide-as in the visual arts as they relate to contemporary society.</p>
<ul class="abs program-list" style="left:540px">
  <li><svg class="arrow" width="7" height="5" viewBox="0 0 7 5"><path d="M0 2.5H6M4 .5 6 2.5 4 4.5" stroke="#333" fill="none" stroke-width=".8"/></svg>Dance</li>
  <li><svg class="arrow" width="7" height="5" viewBox="0 0 7 5"><path d="M0 2.5H6M4 .5 6 2.5 4 4.5" stroke="#333" fill="none" stroke-width=".8"/></svg>English</li>
  <li><svg class="arrow" width="7" height="5" viewBox="0 0 7 5"><path d="M0 2.5H6M4 .5 6 2.5 4 4.5" stroke="#333" fill="none" stroke-width=".8"/></svg>Health &amp; PE</li>
  <li><svg class="arrow" width="7" height="5" viewBox="0 0 7 5"><path d="M0 2.5H6M4 .5 6 2.5 4 4.5" stroke="#333" fill="none" stroke-width=".8"/></svg>Literary Arts</li>
  <li><svg class="arrow" width="7" height="5" viewBox="0 0 7 5"><path d="M0 2.5H6M4 .5 6 2.5 4 4.5" stroke="#333" fill="none" stroke-width=".8"/></svg>Maths</li>
  <li><svg class="arrow" width="7" height="5" viewBox="0 0 7 5"><path d="M0 2.5H6M4 .5 6 2.5 4 4.5" stroke="#333" fill="none" stroke-width=".8"/></svg>Music</li>
</ul>
<ul class="abs program-list" style="left:665px;top:871px">
  <li><svg class="arrow" width="7" height="5" viewBox="0 0 7 5"><path d="M0 2.5H6M4 .5 6 2.5 4 4.5" stroke="#333" fill="none" stroke-width=".8"/></svg>Science</li>
  <li><svg class="arrow" width="7" height="5" viewBox="0 0 7 5"><path d="M0 2.5H6M4 .5 6 2.5 4 4.5" stroke="#333" fill="none" stroke-width=".8"/></svg>Social Sciences</li>
  <li><svg class="arrow" width="7" height="5" viewBox="0 0 7 5"><path d="M0 2.5H6M4 .5 6 2.5 4 4.5" stroke="#333" fill="none" stroke-width=".8"/></svg>Technology</li>
  <li><svg class="arrow" width="7" height="5" viewBox="0 0 7 5"><path d="M0 2.5H6M4 .5 6 2.5 4 4.5" stroke="#333" fill="none" stroke-width=".8"/></svg>Theatre Arts</li>
  <li><svg class="arrow" width="7" height="5" viewBox="0 0 7 5"><path d="M0 2.5H6M4 .5 6 2.5 4 4.5" stroke="#333" fill="none" stroke-width=".8"/></svg>Visual Arts</li>
  <li><svg class="arrow" width="7" height="5" viewBox="0 0 7 5"><path d="M0 2.5H6M4 .5 6 2.5 4 4.5" stroke="#333" fill="none" stroke-width=".8"/></svg>World Languages</li>
</ul>

<footer>
  <div class="abs footer"></div>
  <h4 class="abs footer-head" style="left:92px;top:1030px">QUICK LINKS</h4>
  <ul class="abs footer-links" style="left:93px;top:1047px">
    <li>HOME</li><li>ABOUT RRA</li><li>STUDENTS / PARENTS</li><li>FACULTY / STAFF</li><li>DOCUMENTS / FORMS</li><li>PROGRAMS OF STUDY</li><li>SERVICES</li>
  </ul>
  <h4 class="abs footer-head" style="left:285px;top:1030px">QUICK LINKS</h4>
  <ul class="abs footer-links alt" style="left:286px;top:1051px">
    <li>RRA EMAIL</li><li>CALENDARS</li><li>CONTACT US</li><li>SUBSCRIBE/NEWSLETTERS</li>
  </ul>
  <p class="abs subscribe">SUBSCRIBE TO OUR NEWSLETTER</p>
  <div class="abs field" style="top:1054px"></div>
  <div class="abs field" style="top:1084px"></div>
  <div class="abs socials" aria-label="Social media links"><span></span><span></span><span></span><span></span></div>
</footer>
<p class="abs copyright">Copyright © 2013 Riverbend Regional Academy</p>

</body>
</html>
```